Brightfernrx website

We are a weight loss clinic and we need a website built. please look at these websites for content and style. Just need like 5 pages see samples. AI files of logo are not avail yet so use sample for place set

https://glowshiftstudio.com/
ortanvital.com
https://pinecrestclinicalbodybalance.com/
https://yourslimmingnook.com/
https://qrvskinstudio.com/treatments/weight-loss-injections/

Target Market(s)

Women

Industry/Entity Type

weight loss

Coding

Coded - Design and coding required

Number of Pages Required

5+ page

Requirements
Nice to have
• please make look like a medspa website

```html
<!DOCTYPE html>
<html lang="en">
<head>
<meta charset="utf-8">
<title>Brightfernrx — Weight Loss, Wellness, Rejuvenation</title>
<link href="https://fonts.googleapis.com/css2?family=Cinzel:wght@600;700&family=Raleway:wght@400;500;600;700&display=swap" rel="stylesheet">
<style>
  :root {
    --green: #9ccb4f;
    --green-dark: #6f9a34;
    --blue: #2a8fc1;
    --sky: #27aae1;
    --ink: #222222;
    --line: #e6ecd6;
    --white: #ffffff;
  }
  * { box-sizing: border-box; margin: 0; padding: 0; }
  html, body { width: 802px; height: 1200px; overflow: hidden; background: var(--white); }
  body { position: relative; font-family: "Raleway", sans-serif; color: var(--ink); }
  .serif { font-family: "Cinzel", serif; }

  /* Header */
  .site-header { position: absolute; left: 0; top: 0; width: 802px; height: 69px; border-bottom: 1px solid var(--line); }
  .contact-bar { position: absolute; left: 390px; top: 0; width: 412px; height: 17px; background: var(--green);
    border-bottom-left-radius: 10px; display: flex; align-items: center; color: var(--white); font-size: 7px; letter-spacing: .2px; }
  .contact-item { display: flex; align-items: center; gap: 4px; position: absolute; }
  .contact-item svg { width: 9px; height: 9px; }
  .contact-item.email { left: 22px; }
  .contact-item.phone { left: 174px; }
  .social { position: absolute; left: 288px; display: flex; gap: 13px; }
  .social span { width: 6px; height: 6px; border-radius: 50%; background: var(--white); display: block; }

  .brand { position: absolute; left: 53px; top: 17px; display: flex; align-items: center; gap: 7px; }
  .brand-mark { width: 18px; height: 18px; border-radius: 50%; background: var(--green); }
  .brand-name { font-family: "Raleway", sans-serif; font-weight: 700; font-size: 21px; color: var(--blue); letter-spacing: .5px; }

  .main-nav { position: absolute; right: 53px; top: 37px; display: flex; gap: 13px; font-size: 8.4px; font-weight: 500; letter-spacing: .5px; }

  /* Hero */
  .hero { position: absolute; left: 0; top: 69px; width: 802px; height: 365px; border-bottom: 1px solid #eee; }
  .hero-mark { position: absolute; left: 69px; top: 85px; width: 22px; height: 22px; border-radius: 50%; background: var(--green); opacity: .85; }
  .hero-rule { position: absolute; left: 98px; top: 96px; width: 80px; height: 1px; background: var(--green); }
  .hero-title { position: absolute; left: 69px; top: 137px; width: 300px; white-space: nowrap; font-size: 17.5px; color: var(--blue); font-weight: 700; letter-spacing: 0; }
  .hero-text { position: absolute; left: 69px; top: 179px; width: 282px; font-size: 9.3px; line-height: 16px; }
  .btn-learn { position: absolute; left: 69px; top: 261px; width: 95px; height: 28px; border-radius: 14px;
    background: linear-gradient(90deg, var(--green), var(--blue)); color: var(--white); font-size: 7px; font-weight: 600;
    display: flex; align-items: center; justify-content: center; }
  .hero-photo { position: absolute; left: 385px; top: 0; width: 417px; height: 364px;
    background: linear-gradient(135deg, #d7dde0 0%, #c9cfc9 40%, #1f8a98 62%, #cdd3d6 100%); }

  /* About */
  .about { position: absolute; left: 0; top: 434px; width: 802px; height: 311px; text-align: center; }
  .about-title { position: absolute; left: 0; width: 802px; top: 65px; font-size: 23px; color: var(--blue); font-weight: 700; }
  .about-sub { position: absolute; left: 0; width: 802px; top: 98px; font-size: 10px; font-weight: 600; color: var(--green-dark); }
  .about-text { position: absolute; left: 126px; width: 550px; font-size: 9.2px; line-height: 17px; }
  .about-text.first { top: 131px; }
  .about-text.second { top: 216px; }

  /* Schedule band */
  .schedule { position: absolute; left: 0; top: 745px; width: 802px; height: 120px; background: var(--sky); color: var(--white); }
  .schedule-title { position: absolute; left: 95px; top: 31px; font-size: 23px; line-height: 30px; font-weight: 700; }
  .schedule-divider { position: absolute; left: 268px; top: 22px; width: 1px; height: 76px; background: rgba(255,255,255,.8); }
  .schedule-text { position: absolute; left: 284px; top: 40px; width: 280px; font-size: 8.5px; line-height: 15px; }
  .btn-apply { position: absolute; left: 583px; top: 41px; width: 123px; height: 38px; border-radius: 19px; background: var(--white);
    color: var(--sky); font-size: 10px; font-weight: 600; display: flex; align-items: center; justify-content: center; }

  /* Results */
  .results { position: absolute; left: 0; top: 865px; width: 802px; height: 335px; }
  .results-sub { position: absolute; left: 69px; top: 62px; font-size: 10px; font-weight: 600; color: var(--green-dark); }
  .results-title { position: absolute; left: 69px; top: 86px; font-size: 19.5px; line-height: 26px; color: var(--blue); font-weight: 700; }
  .results-text { position: absolute; left: 69px; top: 150px; width: 292px; font-size: 9.2px; line-height: 17px; text-align: justify; }
  .results-photo { position: absolute; left: 469px; top: 20px; width: 295px; height: 288px;
    background: linear-gradient(160deg, #cfd3d4 0%, #c4c9ca 55%, #b9a48e 100%); }
</style>
</head>
<body>
  <header class="site-header">
    <div class="contact-bar">
      <div class="contact-item email">
        <svg viewBox="0 0 10 10"><circle cx="5" cy="5" r="5" fill="#6f9a34"/><rect x="2.4" y="3.2" width="5.2" height="3.6" fill="#fff"/></svg>
        info@brightfernrx.com
      </div>
      <div class="contact-item phone">
        <svg viewBox="0 0 10 10"><circle cx="5" cy="5" r="5" fill="#6f9a34"/><path d="M3.2 2.8 4.3 2.6 4.8 4 4.2 4.5Q4.8 5.6 5.6 6L6.1 5.4 7.4 6 7.2 7.1Q4.2 7 3.2 2.8Z" fill="#fff"/></svg>
        + 1 100 555 0142
      </div>
      <div class="social" aria-label="Social links"><span></span><span></span><span></span><span></span></div>
    </div>
    <div class="brand">
      <span class="brand-mark"></span>
      <span class="brand-name">Brightfernrx</span>
    </div>
    <nav class="main-nav">
      <span>HOME</span><span>ABOUT</span><span>SERVICES</span><span>TESTIMONIALS</span><span>TREATMENTS</span><span>GALLERY</span><span>CONTACT US</span>
    </nav>
  </header>

  <section class="hero">
    <div class="hero-mark"></div>
    <div class="hero-rule"></div>
    <h1 class="hero-title serif">WELCOME TO BRIGHTFERNRX</h1>
    <p class="hero-text">Lorem ipsum dolor sit amet, consectetur adipiscing elit. Etiam eu turpis molestie, dictum est a, mattis tellus. Sed dignissim, metus nec fringilla accumsan.</p>
    <a class="btn-learn">LEARN MORE</a>
    <div class="hero-photo" role="img" aria-label="Woman in teal leggings running up stadium steps"></div>
  </section>

  <section class="about">
    <h2 class="about-title serif">ABOUT BRIGHTFERNRX</h2>
    <p class="about-sub">MAURIS SIT AMET MAGNA NON LIGULA VESTIBULUM ELEIFEND.</p>
    <p class="about-text first">Lorem ipsum dolor sit amet, consectetur adipiscing elit. Etiam eu turpis molestie, dictum est a, mattis tellus. Sed dignissim, metus nec fringilla accumsan, risus sem sollicitudin lacus, ut interdum tellus elit sed risus. Maecenas eget condimentum velit, sit amet feugiat lectus. Class aptent taciti sociosqu ad litora torquent per conubia nostra, per inceptos himenaeos. Praesent auctor purus luctus enim egestas, ac scelerisque ante pulvinar.</p>
    <p class="about-text second">Curabitur tempor quis eros tempus lacinia. Nam bibendum pellentesque quam a convallis. Sed ut vulputate nisi. Integer in felis sed leo vestibulum venenatis. Suspendisse quis arcu sem. Aenean feugiat ex eu vestibulum vestibulum. Morbi a eleifend magna. Nam metus lacus, porttitor eu mauris a, blandit ultrices nibh.</p>
  </section>

  <section class="schedule">
    <h2 class="schedule-title serif">SCHEDULE A<br>VISIT TODAY!</h2>
    <div class="schedule-divider"></div>
    <p class="schedule-text">Lorem ipsum dolor sit amet, consectetur adipiscing elit. Etiam eu turpis molestie, dictum est a, mattis tellus. Sed dignissim, metus nec fringilla accumsan.</p>
    <a class="btn-apply">APPLY NOW</a>
  </section>

  <section class="results">
    <p class="results-sub">NON LIGULA VESTIBULUM ELEIFEND.</p>
    <h2 class="results-title serif">HOW WE HELP YOU ACHIEVE<br>YOUR DREAM BODY!</h2>
    <p class="results-text">Lorem ipsum dolor sit amet, consectetur adipiscing elit. Etiam eu turpis molestie, dictum est a, mattis tellus. Sed dignissim, metus nec fringilla accumsan, risus sem sollicitudin lacus, ut interdum tellus elit sed risus. Maecenas eget condimentum velit, sit amet feugiat lectus. Class aptent taciti sociosqu ad litora torquent per conubia nostra, per inceptos himenaeos. Praesent auctor purus luctus enim egestas, ac scelerisque ante pulvinar.</p>
    <div class="results-photo" role="img" aria-label="Fit woman in black sportswear lifting a dumbbell"></div>
  </section>
</body>
</html>
```